Flyer-Design für verschiedene Anwendungsfälle bzw. Produkte
Zielgruppe
Wir lösen reale Probleme mit digitalen Technologien wie IoT und KI. In unseren Projekten liefern wir Gesamtlösungen von der Strategieberatung über Konzepterstellung bis zur technischen Umsetzung und dem Betrieb. Integration und Konzeption spielen eine große Rolle, wir sind kein Hardwareanbieter, sondern bauen Komplettlösungen aus Software, Connectivity und Hardware. Unsere Kunden sind gehobener Mittelstand bis Konzern, ab 25 Mio € aufwärts. Oft sind unsere Kunden aus konservativen Branchen. Wir müssen beim Design immer einen Kompromiss aus innovativ und Vertrauen erweckend finden. Unsere Persona ist weiß, männlich, über 50, nicht besonders technologieaffin.
Aufgabenstellung
Wir brauchen eine Flyer-Vorlage für verschiedene Anwendungsfälle bzw. Produkte. Im Anhang sind Beispiele für Produktbeschreibungen, sowie ein Flyer, den wir selbst designet haben.
Ergebnis soll ein Flyer-Design sein, das wir für solche Produkte immer wieder verwenden können, DIN A5 zweiseitig.
Exo2 und Trebuchet sind unsere Schriftarten. Logos habe ich in 2 Formaten angehängt.
Website: tavolu.me
Wenn Sie weitere Ideen haben, sind wir ganz Ohr.
Grafisch bitte nur die Farben grau, schwarz und orange verwenden (grau und orange siehe Logo)

```html
<!DOCTYPE html>
<html lang="de">
<head>
<meta charset="utf-8">
<title>LoRaWAN oder NB-IoT – Flyer</title>
<link rel="stylesheet" href="https://fonts.googleapis.com/css2?family=Exo+2:wght@600;700;800&family=Montserrat:wght@400;500;600;700&display=swap">
<style>
  :root{
    --orange:#e8791e;
    --orange-light:#f2a14f;
    --ink:#232426;
    --graphite:#2e2f32;
    --slate:#33404f;
    --slate-deep:#1f2a38;
    --paper:#f7f7f6;
    --stage:#e4e4e4;
    --white:#ffffff;
  }
  *{box-sizing:border-box;margin:0;padding:0}
  html,body{width:1200px;height:900px;overflow:hidden}
  body{background:var(--stage);font-family:"Montserrat",sans-serif;color:var(--white);
    display:flex;align-items:center;justify-content:center;gap:48px}
  .flyer-page{width:438px;height:620px;position:relative;overflow:hidden;
    box-shadow:0 10px 28px rgba(0,0,0,.18);display:flex;flex-direction:column}
  .flyer-page > *{flex:none}

  /* ---------- Vorderseite ---------- */
  .front{background:var(--ink)}
  .front-hero{position:relative;height:250px}
  .hero-visual{position:absolute;inset:0;
    background:radial-gradient(ellipse 90% 70% at 70% 75%,#6b6b6b 0%,#3c3c3e 45%,var(--graphite) 80%)}
  .brand{position:absolute;top:28px;right:28px;display:flex;align-items:center;gap:8px}
  .brand-dot{width:10px;height:10px;border-radius:50%;background:var(--white)}
  .brand-name{font-family:"Exo 2",sans-serif;font-weight:600;font-size:22px;letter-spacing:4px}
  .front-title{position:absolute;left:30px;top:62px;font-family:"Exo 2",sans-serif;font-weight:800;
    font-size:38px;line-height:1.03}
  .front-subtitle{position:absolute;left:30px;top:182px;font-family:"Exo 2",sans-serif;font-weight:700;
    font-size:15.5px;line-height:1.28}
  .case{position:relative;padding:0 24px 0 28px;font-size:10.5px;line-height:1.32}
  .case-one{background:linear-gradient(180deg,var(--orange),#ec8a33);margin-top:-20px;padding-top:26px;padding-bottom:30px;
    clip-path:polygon(0 20px,58% 20px,62% 0,100% 0,100% 100%,0 100%)}
  .case-two{background:linear-gradient(135deg,var(--slate-deep),var(--slate));flex:1 0 auto;padding-top:30px;padding-bottom:22px;margin-top:-22px;z-index:1;
    clip-path:polygon(0 22px,66% 22px,71% 0,100% 0,100% 100%,0 100%)}
  .case-label{font-family:"Exo 2",sans-serif;font-weight:700;font-size:14px;margin-bottom:3px}
  .case-two .case-label{position:absolute;right:26px;top:3px;margin:0}
  .case-intro{font-weight:500}
  .benefits{list-style:none;margin-top:2px}
  .benefits li{position:relative;padding-left:16px}
  .benefits li::before{content:"";position:absolute;left:2px;top:5px;width:6px;height:6px;border-radius:50%;background:var(--white)}
  .contact-bar{height:58px;background:var(--orange);position:relative;z-index:2;margin-top:-14px;
    clip-path:polygon(0 14px,26% 14px,29% 0,100% 0,100% 100%,0 100%);
    display:grid;grid-template-columns:1fr 1fr;align-content:center;gap:4px 10px;padding:16px 20px 6px;font-size:9.5px}
  .contact-item{display:flex;align-items:center;gap:6px;white-space:nowrap}
  .contact-icon{width:14px;height:14px;flex:none}

  /* ---------- Rückseite ---------- */
  .back{background:var(--paper);color:var(--ink)}
  .back-hero{position:relative;height:250px;padding:22px 34px 0;text-align:center;color:var(--white)}
  .back-hero .hero-visual{background:radial-gradient(ellipse 80% 70% at 40% 80%,#5a5a5c 0%,#343436 50%,var(--graphite) 85%)}
  .back-hero > *:not(.hero-visual){position:relative}
  .tag{display:inline-block;background:var(--orange);color:var(--white);font-family:"Exo 2",sans-serif;
    font-weight:700;font-size:13px;padding:2px 14px;margin-bottom:8px}
  .back-text{font-size:10px;line-height:1.4}
  .back-text p + p{margin-top:4px}
  .hardware-box{margin:26px 24px 0;border:1.5px solid var(--orange);padding:18px 18px 14px;text-align:center;position:relative}
  .hardware-box .tag{position:absolute;top:-12px;left:50%;transform:translateX(-50%)}
  .product-visual{height:64px;margin:10px 20px 0;border-radius:4px;
    background:linear-gradient(90deg,#dcdcdc,#bdbdbd 50%,#dcdcdc)}
  .frontend{margin:24px 24px 0;text-align:center;position:relative}
  .frontend .tag{margin-bottom:6px}
  .web-bar{margin-top:auto;height:40px;background:var(--orange);color:var(--white);display:flex;align-items:center;
    justify-content:center;font-family:"Exo 2",sans-serif;font-weight:700;font-size:14px}
</style>
</head>
<body>

<section class="flyer-page front">
  <div class="front-hero">
    <div class="hero-visual" role="img" aria-label="Nachtaufnahme der Erde aus dem All mit leuchtenden Städten"></div>
    <div class="brand"><span class="brand-dot"></span><span class="brand-name">TAVOLU</span></div>
    <h1 class="front-title">LoRaWAN<br>oder<br>NB-IoT:</h1>
    <p class="front-subtitle">Füllstandsüberwachung<br>und Routenoptimierung<br>Abfallwirtschaft</p>
  </div>

  <div class="case case-one">
    <h2 class="case-label">Fall 1:</h2>
    <p class="case-intro">große öffentliche Container, z.B. Altglas, Altkleider, Altpapier<br>Nutzen und Vorteile</p>
    <ul class="benefits">
      <li>Bürger wissen, zu welchen Containern sie ihren Abfall bringen können</li>
      <li>Entsorger kann optimiert leeren und Kosten sparen</li>
      <li>Containerstandorte können datengestützt erweitert oder reduziert werden</li>
      <li>Weniger wilder Müll</li>
    </ul>
  </div>

  <div class="case case-two">
    <h2 class="case-label">Fall 2:</h2>
    <p class="case-intro">Kleinere städtische Mülleimer, z.B. in Erholungsgebieten<br>Nutzen und Vorteile</p>
    <ul class="benefits">
      <li>Nutzung der Mülleimer ist stark von unregelmäßigen Faktoren wie Wetter oder Veranstaltungen abhängig</li>
      <li>Starr regelmäßige Leerung führt häufig zu Überfüllung und dadurch Umweltverschmutzung, die durch die Anwendung von Sensoren vermieden wird</li>
      <li>Überflüssige Leerungen werden vermieden und dadurch Kosten gespart</li>
    </ul>
  </div>

  <footer class="contact-bar">
    <span class="contact-item">
      <svg class="contact-icon" viewBox="0 0 14 14"><circle cx="7" cy="7" r="7" fill="#fff"/><path d="M4.5 3.5l1.5 0 .6 2-1 .8a5 5 0 0 0 2.2 2.2l.8-1 2 .6v1.5c-3.5.3-6.4-2.6-6.1-6.1z" fill="var(--orange)"/></svg>
      02131 4870220</span>
    <span class="contact-item">
      <svg class="contact-icon" viewBox="0 0 14 14"><circle cx="7" cy="7" r="7" fill="#fff"/><path d="M7 3a2.6 2.6 0 0 0-2.6 2.6C4.4 7.6 7 11 7 11s2.6-3.4 2.6-5.4A2.6 2.6 0 0 0 7 3zm0 3.6a1 1 0 1 1 0-2 1 1 0 0 1 0 2z" fill="var(--orange)"/></svg>
      Hafenweg 8, 40213 Düsseldorf</span>
    <span class="contact-item">
      <svg class="contact-icon" viewBox="0 0 14 14"><circle cx="7" cy="7" r="7" fill="#fff"/><rect x="5" y="3" width="4" height="8" rx="0.8" fill="var(--orange)"/></svg>
      +49 170 4418203</span>
    <span class="contact-item">
      <svg class="contact-icon" viewBox="0 0 14 14"><circle cx="7" cy="7" r="7" fill="#fff"/><rect x="3.5" y="4.5" width="7" height="5" fill="var(--orange)"/><path d="M3.5 4.5L7 7.3l3.5-2.8" fill="none" stroke="#fff" stroke-width=".8"/></svg>
      consulting@tavolu.me</span>
  </footer>
</section>

<section class="flyer-page back">
  <div class="back-hero">
    <div class="hero-visual" role="img" aria-label="Nachtaufnahme der Erde aus dem All mit leuchtenden Städten"></div>
    <span class="tag">Funktionsweise</span>
    <div class="back-text">
      <p>- Im Container werden Sensoren zur Füllstandsmessung angebracht.</p>
      <p>- Der Füllstand wird an eine Bürger-Website/-App gemeldet, die nur „voll“, „fast voll“ und „nicht voll“ anzeigt, sowie bei voll oder fast voll eine möglichst nahe gelegene Alternative.</p>
      <p>- Der Füllstand wird an den Entsorger gemeldet. Hier kann entweder eine Routenoptimierungs-App zur Verfügung gestellt oder die Daten in ein bestehendes Betriebsführungssystem integriert werden.</p>
      <p>- Die Daten werden analysiert, um die regelmäßige Auslastung der Container zu bestimmen und ihre Standorte langfristig zu optimieren.</p>
    </div>
  </div>

  <div class="hardware-box">
    <span class="tag">Hardware</span>
    <p class="back-text">Ultraschall-, Radar- oder optische Sensoren messen den Abstand zwischen sich selbst und der Oberfläche und erkennen so den Füllstand</p>
    <div class="product-visual" role="img" aria-label="Produktfotos verschiedener Füllstandssensoren"></div>
  </div>

  <div class="frontend">
    <span class="tag">Frontend und Benachrichtigungen</span>
    <div class="back-text">
      <p>- Darstellung in einer Web App (für Mobilgeräte und PCs) auf einer Karte für Bürger, mit Anzeige von Alternativen bei vollen Containern</p>
      <p>- Einbindung in Routenoptimierungs- oder Betriebsführungs-Anwendung beim Entsorger</p>
      <p>- Alarmierung bei Überschreitung von Grenzwerten möglich</p>
    </div>
  </div>

  <footer class="web-bar">www.tavolu.me</footer>
</section>

</body>
</html>
```